Banner Ad Design Project

This is a banner Ad Design for MindHarbor 2013, a conference and e-Expo in August 2013 to be held at the Kestrel Bay Events Centre. The conference's focus is on mental excellence and Brain Health. This conference is bringing together personal and community needs, scientific knowledge, and dedicated professionals to create support and solutions for mental excellence and brain-related health issues. Right now in North America, one out of every two individuals is affected by mental health issues: depression, anxiety, learning disorders, memory loss to name a few.
Who we are:
Organization: Willow Lantern Foundation
Industry: Non-profit
Target Market(s)
Age group above 18, parents and health professionals, managers.
Industry/Entity Type
Mental Health
Requirements
Must have
- Please follow the warm design grey as in the design samples.
Nice to have
- Buy tickets and ask your unique questions to the medical panel! Seats are limited!

```html
<!DOCTYPE html>
<html lang="en">
<head>
<meta charset="utf-8">
<title>MindHarbor 2013 Banner</title>
<link rel="stylesheet" href="https://fonts.googleapis.com/css2?family=Oswald:wght@500;600&family=Open+Sans:wght@400;600;700&display=swap">
<style>
  :root {
    --bg-light: #ffffff;
    --bg-warm: #e9e7e3;
    --panel-grey: #d6d3ce;
    --panel-edge: #c7c3bd;
    --brand-navy: #24466f;
    --brand-blue: #2f7fc0;
    --accent-orange: #f5861f;
    --accent-orange-dark: #e06a0c;
    --headline-grey: #5a5654;
    --tag-purple: #7a4f8e;
    --white: #ffffff;
    --photo-light: #d9cfc4;
    --photo-dark: #9aa6b4;
  }
  * { margin: 0; padding: 0; box-sizing: border-box; }
  html, body { width: 1200px; height: 148px; overflow: hidden; background: var(--bg-light); }
  .banner {
    position: relative; width: 1200px; height: 148px; overflow: hidden;
    background: linear-gradient(180deg, var(--bg-light) 0%, var(--bg-warm) 100%);
    font-family: "Open Sans", Arial, sans-serif;
  }
  .brand { position: absolute; left: 23px; top: 34px; }
  .brand-mark {
    position: absolute; left: 0; top: 4px; width: 38px; height: 38px;
    border-radius: 50%; background: var(--brand-blue);
  }
  .brand-name {
    position: absolute; left: 46px; top: 0; white-space: nowrap;
    font-weight: 700; font-size: 33px; line-height: 44px; color: var(--brand-navy);
    letter-spacing: -0.5px;
  }
  .brand-tagline {
    position: absolute; left: 2px; top: 48px; white-space: nowrap;
    font-weight: 600; font-size: 15px; color: var(--brand-blue);
  }
  .speaker-photo {
    position: absolute; left: 379px; top: 0; width: 138px; height: 148px;
    background: linear-gradient(180deg, var(--photo-light) 0%, var(--photo-dark) 100%);
  }
  .headline {
    position: absolute; left: 522px; top: 16px;
    font-family: "Oswald", "Arial Narrow", sans-serif; font-weight: 600;
    font-size: 27px; line-height: 33px; text-transform: uppercase;
    color: var(--headline-grey); white-space: nowrap; text-align: center;
  }
  .headline .highlight { color: var(--accent-orange); }
  .event-details {
    position: absolute; left: 540px; top: 92px; width: 420px;
    font-size: 15.5px; line-height: 20px; color: var(--brand-blue);
    text-align: center; white-space: nowrap;
  }
  .cta-panel {
    position: absolute; left: 972px; top: 0; width: 228px; height: 148px;
    background: linear-gradient(180deg, var(--bg-warm) 0%, var(--panel-grey) 100%);
    border-left: 1px solid var(--panel-edge);
  }
  .seats-tag {
    position: absolute; left: 25px; top: 36px; width: 186px; height: 33px;
    background: var(--white); border-radius: 3px 0 0 3px;
    font-size: 17px; line-height: 33px; text-align: center; color: var(--tag-purple);
  }
  .join-button {
    position: absolute; left: 76px; top: 79px; width: 135px; height: 50px;
    background: linear-gradient(180deg, var(--accent-orange) 0%, var(--accent-orange-dark) 100%);
    border-radius: 3px; color: var(--white);
    font-family: "Oswald", "Arial Narrow", sans-serif; font-weight: 500;
    font-size: 23px; line-height: 50px; text-align: center; text-transform: uppercase;
    text-decoration: none;
  }
</style>
</head>
<body>
  <div class="banner">
    <div class="brand">
      <span class="brand-mark"></span>
      <span class="brand-name">MindHarbor.ca</span>
      <span class="brand-tagline">Mental excellence. Brain health.</span>
    </div>
    <div class="speaker-photo" role="img" aria-label="Portrait photograph of a smiling medical panel speaker"></div>
    <h1 class="headline"><span class="highlight">Buy tickets</span> and ask your unique<br>questions to the medical panel!</h1>
    <p class="event-details">The conference and e-Expo will be held at the<br>Kestrel Bay Events Centre in august 2013.</p>
    <div class="cta-panel">
      <div class="seats-tag">seats are limited!</div>
      <a class="join-button" href="#">Join now</a>
    </div>
  </div>
</body>
</html>
```